Stationery Design

General Brief:
Larkfen Group is a newly established international manufacturing company. We have a manufacturing facility in China and are in the process of building a new facility in Brazil and are expanding into Africa, the Middle East and Western markets by marketing our products through a licensee program. We use production line manufacture processes (similar to the automotive industry) to produce houses, apartments, hotels and accommodation for the resource sector. We will need to be able to differentiate between the various regions that we serve and the market we operate in.

Key Words to describe our business:
International, Global, Professional, Quality, Standard Compliant, Designful, Cost Effective, Experienced

General Brief:
We are looking for good clean design for our letterhead, email signature, Powerpoint presentations, Excel spreadsheets etc. We are looking for templates that can be adopted across the organisation throughout the Microsoft Office suite. Corporate signature files as at November 15 2013 are attached.

Logo Symbolism:
A dot might seem to be an unassuming little thing, the first mark on the pristine sheet of paper. In this case, the dot is a beginning. But see what just happened there? The dot, an essential component in the structure of the sentence, closed it, making it a symbol of ending. Therefore, the dot is both an origination and a conclusion, encompassing all the possibilities of the universe within it, a seed full of potential and a symbol of the supreme being. The dot is also called the "bindhu," which means "drop." The bindhu is a symbol of the absolute, marked on the forehead at the position of the third eye in the place believed to be the seat of the soul. The presence of dots outside or within a symbol can signify the presence of something else. It also acts as reminder of the concept of space and all in all performs as a very positive symbol in the Larkfen Group logo.

Target Market(s)

Governments, NGOs, Developers, Investors

Industry/Entity Type

Accommodation

Font styles to use
Other font styles liked:
• in line with corporate signature (logotype)

Requirements
Must have
• Must adhere to corporate signature style and colour codes such as provided in attached documentation. Please be so kind as to design onscreen previews in RGB colours as per attachment.

```html
<!DOCTYPE html>
<html lang="en">
<head>
<meta charset="utf-8">
<title>Larkfen Group — Stationery System</title>
<link href="https://fonts.googleapis.com/css2?family=Jost:wght@400;500&display=swap" rel="stylesheet">
<style>
  :root {
    --navy: #022f43;
    --cyan: #0aa7e6;
    --paper: #ffffff;
    --rule: #b9bec2;
    --grey: #7d8a93;
    --soft: #c8d3da;
    --font: "Jost", sans-serif;
  }
  * { margin: 0; padding: 0; box-sizing: border-box; }
  html, body { width: 1200px; height: 899px; overflow: hidden; background: var(--paper); }
  body { font-family: var(--font); color: var(--navy); }
  .canvas { position: relative; width: 1200px; height: 899px; }
  .abs { position: absolute; }

  .section-label { position: absolute; font-size: 12px; letter-spacing: 2.6px; font-weight: 400; color: var(--navy); }

  /* wordmark: invented name only, one colour, one weight */
  .wordmark { white-space: nowrap; font-weight: 500; color: var(--navy); line-height: 1; }
  .hero-mark { position: absolute; left: 204px; top: 146px; font-size: 46px; }

  .sheet { position: absolute; }
  .sheet.white { background: var(--paper); border: 1px solid var(--rule); }
  .sheet.dark { background: var(--navy); }
  .disc { position: absolute; border-radius: 50%; background: var(--paper); display: flex; align-items: center; justify-content: center; }
  .disc.dark { background: var(--navy); }
  .disc.dark .wordmark { color: var(--paper); }

  .contact { position: absolute; font-size: 5px; line-height: 1.25; color: var(--grey); letter-spacing: .3px; }
  .contact .name { color: var(--cyan); font-weight: 500; }
  .contact .co { color: var(--cyan); font-weight: 500; margin-top: 4px; }
  .cols { display: flex; gap: 20px; }
  .web { position: absolute; font-size: 6px; letter-spacing: 1px; color: var(--navy); white-space: nowrap; }
  .on-navy .contact, .on-navy .web { color: var(--soft); }

  .slide-title { position: absolute; left: 22px; top: 18px; font-size: 14px; line-height: 1.2; color: var(--paper); letter-spacing: .6px; }
</style>
</head>
<body>
<main class="canvas">

  <div class="hero-mark wordmark">Larkfen Group</div>

  <!-- Email signature -->
  <h2 class="section-label" style="left:675px;top:175px;">EMAIL SIGNATURE</h2>
  <section class="sheet white email-sig" style="left:674px;top:212px;width:224px;height:83px;">
    <div class="disc dark" style="left:12px;top:9px;width:64px;height:64px;">
      <div class="wordmark" style="font-size:7px;">Larkfen Group</div>
    </div>
    <div class="contact" style="left:88px;top:17px;">
      <div class="name">First Lastname</div><div>Title name</div>
      <div class="cols"><div><div class="co">larkfen</div>Address line one<br>Address line two<br>Address line three</div>
      <div style="padding-top:10px;">Phone number one<br>Phone number two<br>Email address</div></div>
    </div>
    <div class="web" style="left:88px;top:61px;">www.larkfen.com</div>
  </section>
  <section class="sheet dark email-sig on-navy" style="left:922px;top:212px;width:224px;height:83px;">
    <div class="disc" style="left:12px;top:9px;width:64px;height:64px;">
      <div class="wordmark" style="font-size:7px;">Larkfen Group</div>
    </div>
    <div class="contact" style="left:88px;top:17px;">
      <div class="name">First Lastname</div><div>Title name</div>
      <div class="cols"><div><div class="co">larkfen</div>Address line one<br>Address line two<br>Address line three</div>
      <div style="padding-top:10px;">Phone number one<br>Phone number two<br>Email address</div></div>
    </div>
  </section>

  <!-- Letterhead -->
  <h2 class="section-label" style="left:37px;top:309px;">LETTERHEAD</h2>
  <section class="sheet dark letterhead-back" style="left:322px;top:379px;width:319px;height:451px;">
    <div class="disc" style="left:89px;top:156px;width:141px;height:141px;">
      <div class="wordmark" style="font-size:15px;">Larkfen Group</div>
    </div>
  </section>
  <section class="sheet white letterhead-front" style="left:37px;top:343px;width:319px;height:450px;">
    <div class="wordmark abs" style="left:22px;top:31px;font-size:15px;">Larkfen Group</div>
    <div class="contact" style="left:22px;top:413px;">
      <div class="cols"><div><div class="name">larkfen</div>Address line one<br>Address line two<br>Address line three</div>
      <div style="padding-top:6px;">Phone number one<br>Phone number two<br>Email address</div></div>
    </div>
    <div class="web" style="left:240px;top:425px;">www.larkfen.com</div>
  </section>

  <!-- Business card -->
  <h2 class="section-label" style="left:722px;top:410px;">BUSINESS CARD</h2>
  <section class="sheet dark card-back" style="left:712px;top:461px;width:136px;height:84px;">
    <div class="disc" style="left:50px;top:23px;width:38px;height:38px;">
      <div class="wordmark" style="font-size:4.5px;">Larkfen Group</div>
    </div>
  </section>
  <section class="sheet white card-front" style="left:596px;top:442px;width:137px;height:84px;">
    <div class="wordmark abs" style="left:10px;top:18px;font-size:8px;">Larkfen Group</div>
    <div class="contact" style="left:86px;top:18px;font-size:4.5px;">
      <div class="name">First Lastname</div><div>Title name</div>
      <div class="co">larkfen</div>Address line one<br>Address line two<br>Address line three
      <div style="margin-top:3px;">Phone number one<br>Phone number two<br>Email address</div>
    </div>
    <div class="web" style="left:11px;top:64px;font-size:4.5px;">www.larkfen.com</div>
  </section>

  <!-- PowerPoint template -->
  <h2 class="section-label" style="left:950px;top:558px;">POWER POINT TEMPLATE</h2>
  <section class="sheet white slide" style="left:825px;top:591px;width:320px;height:240px;">
    <header class="sheet dark on-navy" style="left:-1px;top:-1px;width:320px;height:65px;">
      <div class="slide-title">Powerpoint<br>Slide name</div>
      <div class="disc" style="left:172px;top:10px;width:46px;height:46px;">
        <div class="wordmark" style="font-size:5px;">Larkfen Group</div>
      </div>
      <div class="contact" style="left:227px;top:22px;font-size:3.5px;">
        <div class="cols" style="gap:14px;"><div><span class="name">larkfen</span><br>Address line one<br>Address line two<br>Address line three</div>
        <div style="padding-top:4px;">Phone number one<br>Phone number two<br>Email address</div></div>
      </div>
      <div class="web" style="left:227px;top:40px;font-size:4px;">www.larkfen.com</div>
    </header>
  </section>

</main>
</body>
</html>
```